Exercise Physiologist needs business cards

I have a logo, I need business cards (Sole trader) as I am moving to a new location and would like an updated look. I provide gym based exercise rehabilitation, injury prevention and movement assessments. I have over 13 years experience as an Exercise Physiologist. I would like the cards to look professional but not boring and can be a little different to stand out when sitting with other Allied Health Professional cards.

Target Market(s)

GP's, Allied health practitioners, people with injuries wanting to exercise

Industry/Entity Type

Health And Wellness

Contact Information for Business Card

Megan Dorrit - Exercise Physiologist 0437 582 906
14 Larkspur Bend Rd
West Harrowby
(Door 3, Brannock Fitness)
vantorahealth@maildrop-example.com
socialpage-example.com/Vantora

Requirements
Must have
• I would like to include a section to add next appointment date and time space to the back of the card.
Nice to have
• Rounded corners and a black background on 1 or 2 sides.
Should not have
• Pictures of fit/toned bodies etc

```html
<!DOCTYPE html>
<html lang="en">
<head>
<meta charset="utf-8">
<title>Vantora Health &amp; Rehabilitation – Business Card</title>
<link rel="stylesheet" href="https://fonts.googleapis.com/css2?family=Noto+Serif:wght@400;700&display=swap">
<style>
  :root {
    --backdrop: #595959;
    --card: #f3f4f6;
    --sky: #5aaedf;
    --royal: #2b5fb0;
    --ink-grey: #5f5f5f;
    --rule: #6b6f78;
    --ghost-fill: #e4ebf2;
    --ghost-ring: #dcdfeb;
  }
  * { box-sizing: border-box; margin: 0; padding: 0; }
  html, body {
    width: 1200px; height: 1200px; overflow: hidden;
    background: var(--backdrop);
    font-family: "Noto Serif", Georgia, serif;
  }
  .card {
    position: absolute; left: 174px;
    width: 878px; height: 502px;
    background: var(--card);
    overflow: hidden;
  }
  .card--front { top: 86px; }
  .card--back { top: 614px; }
  .card__art { position: absolute; inset: 0; width: 100%; height: 100%; }

  .brand { position: absolute; display: flex; align-items: center; gap: 14px; }
  .brand__dot {
    width: 100px; height: 100px; border-radius: 50%;
    background: var(--sky); border: 6px solid var(--royal);
  }
  .brand__name {
    font-size: 60px; font-weight: 400; color: var(--royal);
    line-height: 1;
  }
  .card--front .brand { left: 252px; top: 122px; }
  .card--back .brand { left: 238px; top: 62px; }

  .person { position: absolute; left: 97px; top: 292px; }
  .person__name { font-size: 40px; font-weight: 700; color: var(--sky); line-height: 1.1; }
  .person__role { font-size: 21px; color: var(--ink-grey); margin-top: 2px; }

  .contact { position: absolute; left: 392px; top: 294px; list-style: none; }
  .contact__item {
    display: flex; align-items: flex-start; gap: 10px;
    font-size: 24px; color: var(--ink-grey); line-height: 34px;
  }
  .contact__item + .contact__item { margin-top: 6px; }
  .contact__icon { width: 18px; height: 20px; margin-top: 7px; flex: none; fill: var(--sky); }

  .appointment { position: absolute; left: 95px; top: 306px; }
  .appointment__row { display: flex; align-items: flex-end; height: 42px; }
  .appointment__row + .appointment__row { margin-top: 29px; }
  .appointment__label { font-size: 28px; color: var(--royal); width: 72px; line-height: 1; }
  .appointment__line { width: 308px; border-bottom: 1.5px solid var(--rule); margin-bottom: 4px; }
</style>
</head>
<body>

<section class="card card--front">
  <svg class="card__art" viewBox="0 0 878 502" aria-hidden="true">
    <path d="M0 0 H878 V106 C650 60 350 40 0 108 Z" fill="var(--sky)"/>
    <path d="M462 66 Q700 76 878 112 V142 Q700 92 462 66 Z" fill="var(--royal)"/>
  </svg>

  <div class="brand">
    <span class="brand__dot"></span>
    <span class="brand__name">Vantora</span>
  </div>

  <div class="person">
    <h1 class="person__name">Megan Dorrit</h1>
    <p class="person__role">Exercise Physiologist</p>
  </div>

  <ul class="contact">
    <li class="contact__item">
      <svg class="contact__icon" viewBox="0 0 20 20"><path d="M2 8 Q10 1 18 8 L15 10 L13 7 H7 L5 10 Z M4 12 H16 L17 17 H3 Z"/></svg>
      <span>0437 582 906</span>
    </li>
    <li class="contact__item">
      <svg class="contact__icon" viewBox="0 0 20 20"><path d="M10 1 A7 7 0 0 1 17 8 C17 13 10 19 10 19 C10 19 3 13 3 8 A7 7 0 0 1 10 1 Z M10 5 A3 3 0 1 0 10 11 A3 3 0 1 0 10 5 Z" fill-rule="evenodd"/></svg>
      <span>14 Larkspur Bend Rd, West Harrowby<br>(Door 3, Brannock Fitness)</span>
    </li>
  </ul>
</section>

<section class="card card--back">
  <svg class="card__art" viewBox="0 0 878 502" aria-hidden="true">
    <circle cx="790" cy="300" r="228" fill="none" stroke="var(--ghost-ring)" stroke-width="14"/>
    <circle cx="790" cy="300" r="196" fill="var(--ghost-fill)"/>
  </svg>

  <div class="brand">
    <span class="brand__dot"></span>
    <span class="brand__name">Vantora</span>
  </div>

  <div class="appointment">
    <div class="appointment__row">
      <span class="appointment__label">Date</span>
      <span class="appointment__line"></span>
    </div>
    <div class="appointment__row">
      <span class="appointment__label">Time</span>
      <span class="appointment__line"></span>
    </div>
  </div>
</section>

</body>
</html>
```